Bright Lantern Video Production Website

Hi! I need to remake our website design. We want it to be closer to the template we picked http://pixelharbor.example/item/orbitra-multipurpose-responsive-theme/full_screen_preview/8302461

Here is what we have for now:
http://brightlanternvid.example/
http://www.brightlanternvid.example/bright-lantern-video-about-us-2/
http://www.brightlanternvid.example/services/
http://www.brightlanternvid.example/bright-lantern-video-company-page/
http://www.brightlanternvid.example/bright-lantern-video-contact-us/
http://www.brightlanternvid.example/bright-lantern-video-careers-page/

I would be very grateful for suggestions and new design.

Thanks!
Ronja

Target Market(s)

Startups and companies in need for commercials and promo videos

Industry/Entity Type

Video Production

Number of Pages Required

5+ page

Requirements
Must have
• We want to set the tone of an artistic atmosphere and innovational culture.

```html
<!DOCTYPE html>
<html lang="en">
<head>
<meta charset="utf-8">
<title>Bright Lantern Video</title>
<link href="https://fonts.googleapis.com/css2?family=Lato:wght@300;400;700&family=Satisfy&family=Roboto:wght@500&display=swap" rel="stylesheet">
<style>
:root{
  --orange:#f0821e;
  --salmon:#ef8a6c;
  --rose:#e5626a;
  --ink:#222;
  --grey:#8a8a8a;
  --light:#f7f7f7;
  --footer:#1d1d1f;
  --white:#fff;
}
*{margin:0;padding:0;box-sizing:border-box}
html,body{width:1200px;height:2769px;overflow:hidden}
body{position:relative;font-family:'Lato',sans-serif;background:var(--white);color:var(--ink)}
.hero{position:absolute;left:0;top:0;width:1200px;height:840px}
.hero-photo{position:absolute;inset:0;background:linear-gradient(180deg,#9c5a63 0%,#b9695a 18%,#a2553c 34%,#5a3328 55%,#2c2220 78%,#241d1b 100%)}
.hero-accent{position:absolute;left:0;bottom:0;width:100%;height:8px;background:linear-gradient(90deg,#7a3a20,#e05a18 60%,#ff1a1a)}
.nav{position:absolute;left:59px;top:54px;width:1082px;height:86px;border-bottom:1px solid rgba(255,255,255,.35)}
.brand{position:absolute;left:15px;top:4px;display:flex;align-items:center;gap:14px;color:var(--white);font-weight:700;font-size:13px;letter-spacing:.5px}
.brand-dot{width:38px;height:38px;border:2px solid var(--white);border-radius:50%}
.menu{position:absolute;top:16px;left:0;width:100%;font-size:12px;color:var(--white);letter-spacing:.4px}
.menu span{position:absolute}
.menu .active{font-weight:700;border-bottom:2px solid var(--rose);padding-bottom:3px}
.search{position:absolute;left:1040px;top:14px}
.hero-text{position:absolute;left:0;top:288px;width:1200px;text-align:center;color:var(--white);font-weight:300}
.hero-text .welcome{font-size:50px;line-height:60px}
.hero-text .studio{font-size:60px;line-height:80px;color:var(--orange)}
.hero-text .tagline{font-size:34px;line-height:38px;margin-top:8px}
.about{position:absolute;left:0;top:840px;width:1200px;height:535px}
.monitor{position:absolute;left:76px;top:101px;width:470px;height:375px;background:linear-gradient(180deg,#d3d5d6 0%,#d3d5d6 62%,#e1e2e3 100%);border-radius:18px}
.about-copy{position:absolute;left:620px;top:100px;width:476px;text-align:center}
.about-copy h2{font-weight:300;font-size:26px;color:var(--salmon);letter-spacing:.5px}
.about-copy .lead{font-size:14px;font-weight:300;color:var(--grey);margin-top:6px}
.divider{width:130px;height:2px;background:var(--salmon);margin:12px auto 0;opacity:.7}
.about-copy .pitch{font-family:'Satisfy',cursive;font-size:29px;line-height:44px;color:var(--rose);margin-top:24px}
.work{position:absolute;left:0;top:1375px;width:1200px;height:1080px;background:var(--light)}
.work h2{position:absolute;left:0;top:40px;width:1200px;text-align:center;font-weight:400;font-size:21px;color:var(--orange);letter-spacing:.5px}
.work .underline{position:absolute;left:508px;top:73px;width:184px;height:2px;background:var(--orange);opacity:.6}
.reel{position:absolute;width:345px;height:192px;overflow:hidden}
.reel .shot{position:absolute;inset:0}
.reel .bar{position:absolute;left:0;top:0;width:100%;height:44px;background:linear-gradient(180deg,rgba(0,0,0,.75),rgba(0,0,0,0));display:flex;align-items:center;padding:0 12px;gap:10px;color:var(--white);font-family:'Roboto',sans-serif;font-size:17px;white-space:nowrap}
.reel .title{flex:1;overflow:hidden;text-overflow:ellipsis}
.reel .play{position:absolute;left:152px;top:76px;width:42px;height:30px;border-radius:8px;background:rgba(20,20,20,.85)}
.view-more{position:absolute;left:532px;top:1019px;width:136px;height:26px;border:2px solid var(--orange);color:var(--orange);font-size:13px;text-align:center;line-height:22px}
.footer{position:absolute;left:0;top:2455px;width:1200px;height:314px;background:linear-gradient(180deg,#29292b,#1a1a1c);color:var(--white)}
.contact{position:absolute;left:0;top:38px;width:1200px;text-align:center;font-size:17px}
.contact svg{display:block;margin:0 auto}
.footer .rule{position:absolute;left:377px;top:170px;width:446px;height:1px;background:rgba(255,255,255,.2)}
.social{position:absolute;top:196px;width:44px;height:44px;border:3px solid var(--orange);border-radius:50%}
.footer .base{position:absolute;left:59px;top:270px;width:1082px;border-top:1px solid rgba(255,255,255,.2);padding-top:14px;font-size:10px;color:#bbb}
.footer .legal{position:absolute;right:0;top:14px;display:flex;gap:16px}
</style>
</head>
<body>

<header class="hero">
  <div class="hero-photo" role="img" aria-label="Film crew with cameras on tripods at sunset in the desert"></div>
  <nav class="nav">
    <div class="brand"><span class="brand-dot"></span>BRIGHT LANTERN VIDEO</div>
    <div class="menu">
      <span class="active" style="left:456px">HOME</span>
      <span style="left:578px">ABOUT</span>
      <span style="left:696px">SERVICES</span>
      <span style="left:806px">CAREERS</span>
      <span style="left:936px">CONTACT</span>
    </div>
    <svg class="search" width="16" height="16" viewBox="0 0 16 16"><circle cx="6.5" cy="6.5" r="5" fill="none" stroke="#fff" stroke-width="2"/><line x1="10" y1="10" x2="15" y2="15" stroke="#fff" stroke-width="2.4"/></svg>
  </nav>
  <div class="hero-text">
    <div class="welcome">WELCOME TO</div>
    <div class="studio">BRIGHT LANTERN VIDEO</div>
    <div class="tagline">WE DELIVER VIDEO STORIES<br>ABOUT GREAT PRODUCTS</div>
  </div>
  <div class="hero-accent"></div>
</header>

<section class="about">
  <div class="monitor" role="img" aria-label="Illustration of a desktop monitor showing the studio name"></div>
  <div class="about-copy">
    <h2>WHO WE ARE</h2>
    <p class="lead">Bright Lantern Video is a creative agency and a production facility.</p>
    <div class="divider"></div>
    <p class="pitch">To fall in love with your product,<br>users have to understand it.<br>We will help you to explain what is it about,<br>and how it will make a great change.<br>How could they live without it before?</p>
  </div>
</section>

<section class="work">
  <h2>HERE IS HOW IT LOOKS LIKE</h2>
  <div class="underline"></div>

  <div class="reel" style="left:61px;top:142px"><div class="shot" role="img" aria-label="Video still of a beachfront villa by the sea" style="background:linear-gradient(160deg,#8aa3b4,#b9a68c 50%,#6d5a45)"></div><div class="bar"><svg width="18" height="14"><path d="M0 1h18M0 7h18M0 13h12" stroke="#fff" stroke-width="2"/></svg><span class="title">Northwind Films - Real Estate</span><svg width="18" height="18"><circle cx="9" cy="9" r="8" fill="#fff"/><path d="M9 4v5h4" stroke="#222" stroke-width="2" fill="none"/></svg><svg width="18" height="16"><path d="M2 14c2-6 6-8 11-8V2l5 6-5 6v-4c-4 0-8 1-11 4z" fill="#fff"/></svg></div><div class="play"></div></div>

  <div class="reel" style="left:428px;top:142px"><div class="shot" role="img" aria-label="Video still of guests in evening dresses in a golden hall" style="background:linear-gradient(180deg,#6b5630,#8a6b3d 40%,#3a2a1c)"></div><div class="bar"><svg width="18" height="14"><path d="M0 1h18M0 7h18M0 13h12" stroke="#fff" stroke-width="2"/></svg><span class="title">Бархат 2 Смотреть онлайн</span><svg width="18" height="18"><circle cx="9" cy="9" r="8" fill="#fff"/><path d="M9 4v5h4" stroke="#222" stroke-width="2" fill="none"/></svg><svg width="18" height="16"><path d="M2 14c2-6 6-8 11-8V2l5 6-5 6v-4c-4 0-8 1-11 4z" fill="#fff"/></svg></div><div class="play"></div></div>

  <div class="reel" style="left:794px;top:142px"><div class="shot" role="img" aria-label="Video still of a coastal city skyline and beach" style="background:linear-gradient(170deg,#7f9fba,#a9b8bf 45%,#5f8a7f 75%,#c8bfa4)"></div><div class="bar"><svg width="18" height="14"><path d="M0 1h18M0 7h18M0 13h12" stroke="#fff" stroke-width="2"/></svg><span class="title">Northwind Films - Hawaii aerial</span><svg width="18" height="18"><circle cx="9" cy="9" r="8" fill="#fff"/><path d="M9 4v5h4" stroke="#222" stroke-width="2" fill="none"/></svg><svg width="18" height="16"><path d="M2 14c2-6 6-8 11-8V2l5 6-5 6v-4c-4 0-8 1-11 4z" fill="#fff"/></svg></div><div class="play"></div></div>

  <div class="reel" style="left:61px;top:358px"><div class="shot" role="img" aria-label="Video still of an elderly man in a warmly lit room" style="background:linear-gradient(160deg,#4a3a22,#8a6a3a 50%,#3a2416)"></div><div class="bar"><svg width="18" height="14"><path d="M0 1h18M0 7h18M0 13h12" stroke="#fff" stroke-width="2"/></svg><span class="title">The Cinematographer - Reel</span><svg width="18" height="18"><circle cx="9" cy="9" r="8" fill="#fff"/><path d="M9 4v5h4" stroke="#222" stroke-width="2" fill="none"/></svg><svg width="18" height="16"><path d="M2 14c2-6 6-8 11-8V2l5 6-5 6v-4c-4 0-8 1-11 4z" fill="#fff"/></svg></div><div class="play"></div></div>

  <div class="reel" style="left:428px;top:358px"><div class="shot" role="img" aria-label="Video still of a man in a tuxedo" style="background:linear-gradient(180deg,#5a3a1e,#2a1a10 60%,#1a120c)"></div><div class="bar"><svg width="18" height="14"><path d="M0 1h18M0 7h18M0 13h12" stroke="#fff" stroke-width="2"/></svg><span class="title">«Бархат» с 17 марта на экранах</span><svg width="18" height="18"><circle cx="9" cy="9" r="8" fill="#fff"/><path d="M9 4v5h4" stroke="#222" stroke-width="2" fill="none"/></svg><svg width="18" height="16"><path d="M2 14c2-6 6-8 11-8V2l5 6-5 6v-4c-4 0-8 1-11 4z" fill="#fff"/></svg></div><div class="play"></div></div>

  <div class="reel" style="left:794px;top:358px"><div class="shot" role="img" aria-label="Placeholder still for an unavailable video" style="background:radial-gradient(circle at 50% 55%,#d8d8d8,#9a9a9a 80%)"></div><div class="bar"><svg width="18" height="14"><path d="M0 1h18M0 7h18M0 13h12" stroke="#fff" stroke-width="2"/></svg><span class="title">Police Orientation Preparation</span><svg width="18" height="18"><circle cx="9" cy="9" r="8" fill="#fff"/><path d="M9 4v5h4" stroke="#222" stroke-width="2" fill="none"/></svg><svg width="18" height="16"><path d="M2 14c2-6 6-8 11-8V2l5 6-5 6v-4c-4 0-8 1-11 4z" fill="#fff"/></svg></div><div class="play"></div></div>

  <div class="reel" style="left:61px;top:576px"><div class="shot" role="img" aria-label="Video still of a dim concert stage" style="background:linear-gradient(160deg,#1e2418,#3c3a22 50%,#14140e)"></div><div class="bar"><svg width="18" height="14"><path d="M0 1h18M0 7h18M0 13h12" stroke="#fff" stroke-width="2"/></svg><span class="title">Kestrel Mobile 'Explosions'</span><svg width="18" height="18"><circle cx="9" cy="9" r="8" fill="#fff"/><path d="M9 4v5h4" stroke="#222" stroke-width="2" fill="none"/></svg><svg width="18" height="16"><path d="M2 14c2-6 6-8 11-8V2l5 6-5 6v-4c-4 0-8 1-11 4z" fill="#fff"/></svg></div><div class="play"></div></div>

  <div class="reel" style="left:428px;top:576px"><div class="shot" role="img" aria-label="Video still of a crowd at night with city lights" style="background:linear-gradient(160deg,#2a2a2a,#4a4a3a 50%,#1c2a3a)"></div><div class="bar"><svg width="18" height="14"><path d="M0 1h18M0 7h18M0 13h12" stroke="#fff" stroke-width="2"/></svg><span class="title">Ridgeway 'Crowd Rider'</span><svg width="18" height="18"><circle cx="9" cy="9" r="8" fill="#fff"/><path d="M9 4v5h4" stroke="#222" stroke-width="2" fill="none"/></svg><svg width="18" height="16"><path d="M2 14c2-6 6-8 11-8V2l5 6-5 6v-4c-4 0-8 1-11 4z" fill="#fff"/></svg></div><div class="play"></div></div>

  <div class="reel" style="left:794px;top:576px"><div class="shot" role="img" aria-label="Video still of a figure walking through an ornate hallway" style="background:linear-gradient(160deg,#4a4a3a,#8a8a70 45%,#2a2a22)"></div><div class="bar"><svg width="18" height="14"><path d="M0 1h18M0 7h18M0 13h12" stroke="#fff" stroke-width="2"/></svg><span class="title">Marquee beyond Channels</span><svg width="18" height="18"><circle cx="9" cy="9" r="8" fill="#fff"/><path d="M9 4v5h4" stroke="#222" stroke-width="2" fill="none"/></svg><svg width="18" height="16"><path d="M2 14c2-6 6-8 11-8V2l5 6-5 6v-4c-4 0-8 1-11 4z" fill="#fff"/></svg></div><div class="play"></div></div>

  <div class="reel" style="left:61px;top:792px"><div class="shot" role="img" aria-label="Video still of a party in purple light" style="background:linear-gradient(160deg,#3a2a6a,#8a5ac0 50%,#2a1a4a)"></div><div class="bar"><svg width="18" height="14"><path d="M0 1h18M0 7h18M0 13h12" stroke="#fff" stroke-width="2"/></svg><span class="title">Fizzle 'Party'</span><svg width="18" height="18"><circle cx="9" cy="9" r="8" fill="#fff"/><path d="M9 4v5h4" stroke="#222" stroke-width="2" fill="none"/></svg><svg width="18" height="16"><path d="M2 14c2-6 6-8 11-8V2l5 6-5 6v-4c-4 0-8 1-11 4z" fill="#fff"/></svg></div><div class="play"></div></div>

  <div class="reel" style="left:428px;top:792px"><div class="shot" role="img" aria-label="Video still of people in a sandy outdoor scene" style="background:linear-gradient(160deg,#6a5a3a,#a08a60 50%,#4a3a24)"></div><div class="bar"><svg width="18" height="14"><path d="M0 1h18M0 7h18M0 13h12" stroke="#fff" stroke-width="2"/></svg><span class="title">Metro de Solara</span><svg width="18" height="18"><circle cx="9" cy="9" r="8" fill="#fff"/><path d="M9 4v5h4" stroke="#222" stroke-width="2" fill="none"/></svg><svg width="18" height="16"><path d="M2 14c2-6 6-8 11-8V2l5 6-5 6v-4c-4 0-8 1-11 4z" fill="#fff"/></svg></div><div class="play"></div></div>

  <div class="reel" style="left:794px;top:792px"><div class="shot" role="img" aria-label="Video still of a tablet screen in dark green light" style="background:linear-gradient(160deg,#0e1a14,#2a3a30 55%,#101410)"></div><div class="bar"><svg width="18" height="14"><path d="M0 1h18M0 7h18M0 13h12" stroke="#fff" stroke-width="2"/></svg><span class="title">Tanager Flex "Pursuit"</span><svg width="18" height="18"><circle cx="9" cy="9" r="8" fill="#fff"/><path d="M9 4v5h4" stroke="#222" stroke-width="2" fill="none"/></svg><svg width="18" height="16"><path d="M2 14c2-6 6-8 11-8V2l5 6-5 6v-4c-4 0-8 1-11 4z" fill="#fff"/></svg></div><div class="play"></div></div>

  <div class="view-more">view more &#8964;</div>
</section>

<footer class="footer">
  <div class="contact">
    <svg width="14" height="14" viewBox="0 0 14 14"><path d="M3 1l2 3-1.5 1.5c1 2 2.5 3.5 4.5 4.5L9.5 8.5l3 2-1 2.5C6 13 1 8 1 2.5z" fill="#fff"/></svg>
    <div style="margin-top:6px">+14245550187</div>
    <svg width="20" height="14" viewBox="0 0 20 14" style="margin-top:10px"><rect x="1" y="1" width="18" height="12" fill="none" stroke="#fff" stroke-width="2"/><path d="M1 1l9 7 9-7" fill="none" stroke="#fff" stroke-width="2"/></svg>
    <div style="margin-top:4px">info@brightlanternvid.example</div>
  </div>
  <div class="rule"></div>
  <span class="social" style="left:421px"></span>
  <span class="social" style="left:500px"></span>
  <span class="social" style="left:578px"></span>
  <span class="social" style="left:657px"></span>
  <span class="social" style="left:735px"></span>
  <div class="base">Copyright © 2016 All rights reserved.
    <div class="legal"><span>Terms &amp; Conditions</span><span>Privacy Policy</span><span>Refund Policy</span><span>Footer Menu</span></div>
  </div>
</footer>

</body>
</html>
```